Mara Lindqvist Advisory Business Cards

Hi - using the information and logo provided I require a two sided business card designed with the following information. The business card is a 'mini card' 3.5" x 1.25".

Front of card should be the logo attached but inverted (so the background is the peach colour and the logo white).

Back should have these details. If we can't fit the Instragram and Facebook part can we just put the little logos.

Mara Lindqvist

Art and Design Consultant
Dealer - Curator - Events - Styling - Creative Sourcing

P: 0438 519 207
E: mara@maralindqvistadvisory.com
W: www.maralindqvistadvisory.com
I (instagram image please): maralindqvistadvisory F (Facebook image please): MaraLindqvistAdvisor

Target Market(s)

Galleries, artists, art buyers, interior design clients, event managers, creative types

Industry/Entity Type

Business

```html
<!DOCTYPE html>
<html lang="en">
<head>
<meta charset="utf-8">
<title>Mara Lindqvist Advisory – Mini Business Card</title>
<link rel="stylesheet" href="https://fonts.googleapis.com/css2?family=Tinos:wght@400&display=swap">
<style>
  :root {
    --backdrop: #8a7a70;
    --card-black: #0b0b0b;
    --card-black-soft: #1c1c1c;
    --card-white: #ffffff;
    --peach: #f2b99c;
    --glow: rgba(255, 255, 255, 0.22);
    --brand-grey: #8c8c8c;
    --rule-grey: #5a5a5a;
    --rule-light: #e2e2e2;
    --band-rule: #3a3a3a;
    --ink: #1a1a1a;
    --text-white: #f4f4f4;
    --muted: #8f8f8f;
    --handle-square: #9a8a7c;
  }
  * { box-sizing: border-box; margin: 0; padding: 0; }
  html, body { width: 1200px; height: 960px; overflow: hidden; }
  body {
    background: var(--backdrop);
    font-family: "Tinos", "Times New Roman", serif;
    position: relative;
  }

  .card { position: absolute; width: 866px; height: 310px; overflow: hidden; }

  /* Front */
  .card-front {
    left: 50px; top: 50px;
    background:
      radial-gradient(ellipse 240px 170px at 443px 80px, var(--glow), transparent 70%),
      linear-gradient(180deg, var(--card-black-soft), var(--card-black));
  }
  .front-mark {
    position: absolute; left: 393px; top: 22px;
    width: 100px; height: 100px; border-radius: 50%;
    background: var(--peach);
  }
  .front-brand {
    position: absolute; left: 0; right: 0; top: 156px;
    text-align: center; font-size: 25px; letter-spacing: 5px;
    color: var(--brand-grey); text-transform: uppercase;
  }
  .front-rule {
    position: absolute; left: 93px; width: 694px; height: 1px;
    background: var(--rule-grey);
  }
  .front-rule.r1 { top: 214px; }
  .front-rule.r2 { top: 251px; }
  .front-rule.r3 { top: 289px; }
  .front-name {
    position: absolute; left: 0; right: 0; top: 216px;
    text-align: center; color: var(--text-white); font-size: 28px;
  }
  .front-name .role { font-size: 24px; }
  .front-services {
    position: absolute; left: 0; right: 0; top: 259px;
    text-align: center; color: var(--muted); font-size: 18px;
  }

  /* Back */
  .card-back { left: 299px; top: 462px; background: var(--card-white); }
  .back-top-rule {
    position: absolute; left: 28px; width: 810px; top: 28px; height: 1px;
    background: var(--rule-light);
  }
  .back-mark {
    position: absolute; left: 135px; top: 52px;
    width: 90px; height: 90px; border-radius: 50%;
    background: var(--peach);
  }
  .back-brand {
    position: absolute; left: 20px; width: 300px; top: 158px;
    text-align: center; font-size: 16px; letter-spacing: 2.5px;
    color: var(--brand-grey); text-transform: uppercase;
  }
  .back-divider {
    position: absolute; left: 325px; top: 48px; width: 3px; height: 156px;
    background: linear-gradient(180deg, transparent, #2a2a2a 30%, #2a2a2a 70%, transparent);
  }
  .contact-list { position: absolute; left: 367px; top: 66px; list-style: none; }
  .contact-list li { font-size: 22px; color: var(--ink); line-height: 41px; }

  .handle-band {
    position: absolute; left: 0; right: 0; top: 216px; bottom: 0;
    background: var(--card-black);
  }
  .handle-rule {
    position: absolute; left: 28px; width: 812px; height: 1px;
    background: var(--band-rule);
  }
  .handle-rule.r1 { top: 16px; }
  .handle-rule.r2 { top: 67px; }
  .handle-item {
    position: absolute; top: 27px; display: flex; align-items: center; gap: 18px;
    color: var(--text-white); font-size: 24px; line-height: 30px;
  }
  .handle-item.handle-left { left: 53px; }
  .handle-item.handle-right { left: 504px; }
  .handle-square {
    width: 30px; height: 30px; border-radius: 4px;
    background: var(--handle-square);
  }
  .handle-sep {
    position: absolute; left: 440px; top: 27px;
    color: var(--text-white); font-size: 24px; line-height: 30px;
  }
</style>
</head>
<body>

<section class="card card-front" aria-label="Card front">
  <div class="front-mark"></div>
  <div class="front-brand">Mara Lindqvist Advisory</div>
  <div class="front-rule r1"></div>
  <p class="front-name">Mara Lindqvist <span class="role">(Art and Design Consultant)</span></p>
  <div class="front-rule r2"></div>
  <p class="front-services">Dealer | Curator | Events | Styling | Creative Sourcing</p>
  <div class="front-rule r3"></div>
</section>

<section class="card card-back" aria-label="Card back">
  <div class="back-top-rule"></div>
  <div class="back-mark"></div>
  <div class="back-brand">Mara Lindqvist Advisory</div>
  <div class="back-divider"></div>
  <ul class="contact-list">
    <li>Phone: 0438 519 207</li>
    <li>Email: mara@maralindqvistadvisory.com</li>
    <li>Web: www.maralindqvistadvisory.com</li>
  </ul>
  <div class="handle-band">
    <div class="handle-rule r1"></div>
    <div class="handle-item handle-left"><span class="handle-square"></span>MaraLindqvistAdvisor</div>
    <span class="handle-sep">|</span>
    <div class="handle-item handle-right"><span class="handle-square"></span>maralindqvistadvisory</div>
    <div class="handle-rule r2"></div>
  </div>
</section>

</body>
</html>
```